Divorce Lawyer Creative Business Card Design Project

Need a fresh look for our business cards that incorporates our current logo. We have three attorneys and six staff. Some will also use a Q/R Code (which is personal to the staff member) and that should be incorporated into the design so that we have a "with Q/R Code option" and a "without Q/R Code option"
While our business is serious and we want to be professional, we also welcome a bit of creativity and "fun." See http://cardowlet.example/creative-business-card-for-a-divorce-lawyer/ for a unique divorce lawyer business card. It is cool but the card itself is boring...
We add new people, change titles, some of our staff get married (and divorced) and have name changes and we need the ability to use a design template that you provide to make these changes ourselves. We usually print our cards at Plumo Press.
I have uploaded a file that contains a sample of our current front and back of the business card as well as a sample Q/R Contact code to be included on a card. Obviously, we like the design that we have which should give you a feel for us but we are ready for a fresh look.
If you can't provide a design that we can manipulate, we will need .eps, .pdf, and .jpg files for three attorneys and six staff.
Updates
- Layout for this card is really nice: http://blog.inkhollow.example/wp-content/uploads/2013/03/torva-business-card.jpg
- This is creative: http://pinboardly.example/pin/572810394628150443/ but I don't really like it.
- Plastic is kind of cool: http://pinboardly.example/pin/572810394628937216/
- DISLIKE: http://promoglobe.example/sites/default/files/styles/media/public/images/Lawyerbusinesscard.jpg?itok=ZrTmWe-k
- This is really cool but I fear the printing costs would be too high: http://pinboardly.example/pin/46192837504618352/
- I am not opposed to different but similar designs: See http://www.folioverse.example/gallery/ZEP-Business-Cards/8263045
Industry/Entity Type
Lawyer
Requirements
Must have
- Our Logo
Person's Full Name
Title
Phone #
Fax #
Email
Web Address

```html
<!DOCTYPE html>
<html lang="en">
<head>
<meta charset="utf-8">
<title>Hollis Law PLLC – Business Card</title>
<link href="https://fonts.googleapis.com/css2?family=Sorts+Mill+Goudy:ital@0;1&display=swap" rel="stylesheet">
<style>
  :root {
    --backdrop: #a7a8ab;
    --card: #f1f1f2;
    --ink-dark: #1f1f22;
    --ink-soft: #77777b;
    --figure-tone: #cfcfd2;
    --mark: #2e4a7c;
    --perforation: #1a1a1a;
  }
  * { margin: 0; padding: 0; box-sizing: border-box; }
  html, body {
    width: 1200px; height: 900px; overflow: hidden;
    background: var(--backdrop);
    font-family: "Sorts Mill Goudy", Georgia, serif;
  }
  .stage { position: relative; width: 1200px; height: 900px; }

  .card {
    position: absolute;
    background: var(--card);
    overflow: hidden;
  }
  .card--whole { left: 56px; top: 330px; width: 524px; height: 307px; }
  .card--stub  { left: 611px; top: 330px; width: 79px;  height: 307px; }
  .card--main  { left: 701px; top: 330px; width: 447px; height: 307px; }

  .perforation {
    position: absolute; left: 78px; top: 0; height: 100%;
    border-left: 2px dashed var(--perforation);
  }

  .couple-figures {
    position: absolute; top: 104px; height: 131px;
    background: var(--figure-tone);
  }
  .card--whole .couple-figures { left: 19px; width: 113px; }
  .card--stub  .couple-figures { left: 20px; width: 59px; }
  .card--main  .couple-figures { left: 0; width: 55px; }

  .details {
    position: absolute; right: 37px; top: 24px;
    text-align: right; color: var(--ink-soft);
  }
  .card--main .details { right: 36px; }

  .firm-mark {
    display: flex; justify-content: flex-end; align-items: center;
    gap: 8px; height: 96px;
  }
  .firm-mark__square { width: 16px; height: 16px; background: var(--mark); }
  .firm-mark__name { font-size: 19px; color: var(--mark); }

  .person-name {
    margin-top: 6px;
    font-style: italic; font-size: 23px; line-height: 1;
    color: var(--ink-dark);
  }
  .card--main .person-name { color: var(--ink-soft); }
  .person-title { font-size: 14px; color: var(--ink-dark); line-height: 1.2; }
  .card--main .person-title { color: var(--ink-soft); }

  .contact { font-size: 15px; line-height: 20px; }
  .contact--address { margin-top: 16px; }
  .contact--po { margin-top: 10px; }
  .contact--lines { margin-top: 10px; }
</style>
</head>
<body>
<main class="stage">

  <section class="card card--whole">
    <div class="couple-figures" role="img" aria-label="Pictogram of a woman and a man holding hands"></div>
    <div class="perforation"></div>
    <div class="details">
      <div class="firm-mark"><span class="firm-mark__square"></span><span class="firm-mark__name">Hollis Law PLLC</span></div>
      <p class="person-name">Owen Carlisle Bennett</p>
      <p class="person-title">Managing Attorney</p>
      <p class="contact contact--address">Counsel Row-Suite G, 218 Alder Street<br>Brookhaven, NC 28499</p>
      <p class="contact contact--po">P.O. Box 451, Brookhaven, NC 28498</p>
      <p class="contact contact--lines">Phone: (555) 014-2278, Fax: (555) 014-6391<br>obennett@hollisfamilylaw.example</p>
    </div>
  </section>

  <section class="card card--stub">
    <div class="couple-figures" role="img" aria-label="Pictogram of a woman, torn away from the card"></div>
  </section>

  <section class="card card--main">
    <div class="couple-figures" role="img" aria-label="Pictogram of a man standing alone"></div>
    <div class="details">
      <div class="firm-mark"><span class="firm-mark__square"></span><span class="firm-mark__name">Hollis Law PLLC</span></div>
      <p class="person-name">Owen Carlisle Bennett</p>
      <p class="person-title">Managing Attorney</p>
      <p class="contact contact--address">Counsel Row-Suite G, 218 Alder Street<br>Brookhaven, NC 28499</p>
      <p class="contact contact--po">P.O. Box 451, Brookhaven, NC 28498</p>
      <p class="contact contact--lines">Phone: (555) 014-2278, Fax: (555) 014-6391<br>obennett@hollisfamilylaw.example</p>
    </div>
  </section>

</main>
</body>
</html>
```